Comic, writer, and entrepreneur based in Los Angeles, CA

UPDATED BRIEF:

Need a PROFESSIONAL yet simultaneously sexy business card that will inspire those to go to my social media accounts and follow me.

Need all of my social media (logos on card, please) As well as my picture, which I will provide.

If there is a way where you could scan the business card from your phone and it would take you to the social media accounts that would be great too!

My goal is to get a comedy writing job at the Evening Desk or LNB and also go on Otter Pond once my app is fully functional and created.

But the business card is just something to give people when I am making connections in both the entrepreneurial world as well as the comedy world so it has to help me stand out in that way :).

#: 555-284-7193
Email: kbellamy@mail.northfen.edu
Snapgrid: Korinne_Q.P
Chirpline: @ThePelicanLedger
Crafterly: Kori’s Quirky Tops (website: https://www.crafterly-example.com/shop/KorisTp?ref=pr_shop_more)
ClipCastle: The Gagsmith (website: https://www.clipcastle-example.com/channel/QWzRtp4nL-vbKJyymu7gfe9B )
Friendwall: /korinne.bellamy.71204
Website App: QuickFixPals.net (app in progress. Need emails to make a prototype.)

Target Market(s)

Talent agents needing TV writers and TV comedy personalities. Investors for my app.

Industry/Entity Type

Tv

Contact Information for Business Card

Can be double or single sided, whichever looks best. Green is my favorite color but I am open to anything. Maybe silver and green?! Just make it classy and sexy.

Colors

Designer to choose colors to be used in the design.

Requirements
Must have
• Chirpline: ThePelicanLedger
• Snapgrid: Korinne_q.p
• Clipcastle: The Gagsmith
• Email: kbellamy@mail.northfen.edu
• Phone: 555-284-7193
• writer, comic, entrepreneur--or--comedy writer and entrepeneur
Nice to have
• Make me standout. I'm a star ;-). Please check out my social media for files or ideas. Thanks.

```html
<!DOCTYPE html>
<html lang="en">
<head>
<meta charset="utf-8">
<title>Marlow Pryce – Business Card</title>
<link rel="stylesheet" href="https://fonts.googleapis.com/css2?family=Questrial&family=Oswald:wght@500&display=swap">
<style>
  :root {
    --backdrop: #161616;
    --card-white: #ffffff;
    --accent-pink: #e0368f;
    --ink-grey: #555555;
    --back-pink-deep: #dc2f93;
    --back-pink: #e6479e;
    --back-pink-light: #ea5aa8;
    --text-light: #ffffff;
  }
  * { margin: 0; padding: 0; box-sizing: border-box; }
  html, body {
    width: 1200px;
    height: 897px;
    overflow: hidden;
    background: var(--backdrop);
  }
  .stage {
    position: relative;
    width: 1200px;
    height: 897px;
  }
  .card {
    position: absolute;
    left: 303px;
    width: 595px;
    height: 339px;
    overflow: hidden;
    box-shadow: 0 4px 14px rgba(0, 0, 0, 0.6);
  }
  /* Front side */
  .card--front {
    top: 92px;
    background: var(--card-white);
    font-family: "Questrial", sans-serif;
  }
  .front__glow {
    position: absolute;
    right: -30px;
    top: -110px;
    width: 340px;
    height: 340px;
    border-radius: 50%;
    background: radial-gradient(circle at 55% 45%, #f4f4f4 0%, #fafafa 45%, rgba(255,255,255,0) 72%);
  }
  .front__name {
    position: absolute;
    left: 37px;
    top: 57px;
    font-size: 24px;
    letter-spacing: 1.4px;
    color: var(--accent-pink);
    font-weight: 400;
  }
  .front__role {
    position: absolute;
    left: 37px;
    top: 89px;
    font-size: 15.5px;
    letter-spacing: 0.9px;
    color: var(--ink-grey);
    -webkit-text-stroke: 0.3px var(--ink-grey);
  }
  .front__rule {
    position: absolute;
    left: 38px;
    top: 141px;
    width: 47px;
    height: 2px;
    background: var(--accent-pink);
  }
  .front__contacts {
    position: absolute;
    left: 37px;
    top: 176px;
    list-style: none;
    font-size: 15.5px;
    letter-spacing: 0.9px;
    line-height: 24px;
    color: var(--ink-grey);
  }
  .front__socials {
    position: absolute;
    left: 37px;
    top: 240px;
    list-style: none;
    font-size: 13.5px;
    letter-spacing: 0.8px;
    line-height: 22px;
    color: var(--ink-grey);
  }
  .front__label { color: var(--accent-pink); }

  /* Back side */
  .card--back {
    top: 469px;
    background:
      radial-gradient(ellipse at 70% 20%, var(--back-pink-light) 0%, rgba(234,90,168,0) 60%),
      linear-gradient(135deg, var(--back-pink-deep) 0%, var(--back-pink) 45%, var(--back-pink) 100%);
  }
  .back__portrait {
    position: absolute;
    left: 385px;
    top: 23px;
    width: 180px;
    height: 316px;
    border-radius: 60px 60px 0 0;
    background: linear-gradient(180deg, rgba(230,71,158,0) 0%, rgba(43,43,46,0.55) 35%, rgba(43,43,46,0.7) 60%, rgba(60,80,130,0.55) 100%);
  }
  .back__tagline {
    position: absolute;
    left: 38px;
    top: 278px;
    font-family: "Oswald", sans-serif;
    font-weight: 500;
    font-size: 27px;
    letter-spacing: -0.3px;
    transform: scaleX(0.86);
    transform-origin: left center;
    color: var(--text-light);
    white-space: nowrap;
  }
</style>
</head>
<body>
<main class="stage">
  <section class="card card--front">
    <div class="front__glow"></div>
    <h1 class="front__name">MARLOW PRYCE</h1>
    <p class="front__role">WRITER, COMIC, ENTREPRENEUR</p>
    <div class="front__rule"></div>
    <ul class="front__contacts">
      <li><span class="front__label">Phone:</span> 555-284-7193</li>
      <li><span class="front__label">Email:</span> kbellamy@mail.northfen.edu</li>
    </ul>
    <ul class="front__socials">
      <li><span class="front__label">Chirpline:</span> @ThePelicanLedger</li>
      <li><span class="front__label">Snapgrid:</span> Korinne_q.p</li>
      <li><span class="front__label">ClipCastle:</span> The Gagsmith</li>
    </ul>
  </section>

  <section class="card card--back">
    <div class="back__portrait" role="img" aria-label="Portrait photo of the writer in a leather jacket and jeans, smiling against a pink wall"></div>
    <p class="back__tagline">WRITER, COMIC, ENTREPRENEUR</p>
  </section>
</main>
</body>
</html>
```